Creation of a Facebook cover graphic

We need a Facebook cover graphic for a page that will be used to test the market for an online training product.

The Product

The subject of the training is the basic online marketing. The training will be delivered online rather than at a venue.

The name of the website is www.tallowfinchhub.com. PLEASE NOTE We have owned the site domain for a while and the current content is 'NOT' representative of the new product. If Quillbarrow deliver on this project we will be back for the website and logo designs! please note we have included a draft logo concept file attachment with the brief.

Design Details

The cover graphic will be viewed on desktop, tablet and mobile. We have tried to give you a brief that guarantees the profile looks good and is readable on mobile. The design is bold and simple in order to enhance viewing the graphic on mobile.

We have included a draft graphic (Both as psd and png). This only shows layout and content. The draft graphic is mainly text based.

We have also included a concept file for the logo. You may want to incorporate the target and arrow icon contained in that file into the design.

Creating a design optimised for mobile is perhaps more challenging than larger formats. Feel free to designs with the following elements: Backgrounds; shapes; gradients and font/text effects - however try and retain a flat and simple design

Graphic size: 828px x 315px – we prefer this size rather than the mobile specific size. It actually renders best across all devices.
Place the design in between 174px & 650px horizontally as this gives best viewing on mobile. Backgrounds can extend across the whole graphic.
Web resolution

There are 2 section to the design:

Section 1. Title ‘The Bright Harbour Crew’
Section 2. Sub title ’Solving online marketing needs’ and to do listing

For the logo colouring and background we would prefer:

Background colour: #236d99 will be our main corporate colour. Other colours are #00456e, #236d99 and # 82bcd0.
Text colour : white or white with a shade of blue. You may contrast text colour of section 1 and section 2.

Fonts : We have two font styles in the draft (Arial Black and Arial Nova). The mobile first design requires the fonts to be very simple so as the text can be read on mobile devices. You can try similar such as Helvetica, Lato etc.
Icons etc : There are 3 ticks against each element of the to do list. Feel free to creative how you want to work with these.

Examples

The Quillbarrow graphic included in the files is a good example of simplicity and flat design.

Target Market(s)

Our clients will be business owners and managers. Generally, one person, small and medium sized businesses.
Gender : Both male and female.
Typical ages : 35-65
They favour simplicity, functionality and boldness - rather than elegance or sophistication

Industry/Entity Type

Marketing

Font styles to use
Sans Serif

Requirements
Must have
• View well on mobile devices
• Text readable on mobile devices
• Simplicity
• Flatter type of design
Nice to have
• Not really a design idea. Would like some feedback on whether our design brief was useful for you as designers.
Should not have
• Complex and finely detailed design

```html
<!DOCTYPE html>
<html lang="en">
<head>
<meta charset="utf-8">
<title>The Bright Harbour Crew – Cover</title>
<link href="https://fonts.googleapis.com/css2?family=Archivo+Black&family=Arimo:wght@400;700&display=swap" rel="stylesheet">
<style>
  :root {
    --navy: #07528a;
    --navy-edge: #6f9fc0;
    --sky: #82bcd0;
    --sky-soft: #c7dfe8;
    --brand-blue: #3a8fd0;
    --white: #ffffff;
    --page: #ffffff;
  }
  html, body {
    margin: 0;
    width: 1200px;
    height: 1200px;
    overflow: hidden;
    background: var(--page);
  }
  .canvas {
    position: relative;
    width: 1200px;
    height: 1200px;
  }
  .cover {
    position: absolute;
    left: 68px;
    top: 398px;
    width: 1064px;
    height: 404px;
    background: var(--white);
    overflow: hidden;
  }
  .cover-shapes {
    position: absolute;
    inset: 0;
  }
  .world-area {
    position: absolute;
    left: 828px;
    top: 104px;
    width: 236px;
    height: 160px;
    border-radius: 40px 60px 30px 50px;
    background: radial-gradient(ellipse at center, var(--sky) 0%, rgba(130,188,208,0.55) 60%, rgba(130,188,208,0) 100%);
  }
  .title {
    position: absolute;
    left: 268px;
    top: 42px;
    margin: 0;
    font-family: "Archivo Black", "Arial Black", sans-serif;
    font-size: 36px;
    line-height: 1;
    letter-spacing: 0.5px;
    color: var(--white);
  }
  .subtitle {
    position: absolute;
    left: 264px;
    top: 114px;
    margin: 0;
    font-family: "Arimo", Arial, sans-serif;
    font-size: 35px;
    line-height: 1;
    color: var(--white);
  }
  .todo-list {
    position: absolute;
    left: 274px;
    top: 180px;
    margin: 0;
    padding: 0;
    list-style: none;
    font-family: "Arimo", Arial, sans-serif;
    font-size: 35px;
    line-height: 1;
    color: var(--white);
  }
  .todo-item {
    display: flex;
    align-items: center;
    height: 65px;
    margin-top: -14px;
  }
  .todo-item:first-child { margin-top: 0; }
  .tick {
    width: 24px;
    height: 24px;
    margin-right: 23px;
    margin-top: 12px;
    flex: none;
  }
  .brand {
    position: absolute;
    left: 774px;
    top: 300px;
    display: flex;
    align-items: center;
    gap: 10px;
    font-family: "Arimo", Arial, sans-serif;
    font-weight: 700;
    font-size: 33px;
    line-height: 1;
    color: var(--brand-blue);
    letter-spacing: 0.5px;
  }
  .brand-dot {
    width: 22px;
    height: 22px;
    border-radius: 50%;
    background: var(--brand-blue);
    flex: none;
  }
</style>
</head>
<body>
<div class="canvas">
  <section class="cover">
    <svg class="cover-shapes" viewBox="0 0 1064 404" width="1064" height="404" aria-hidden="true">
      <polygon points="840,40 1064,0 1064,30 852,70" fill="var(--sky-soft)"/>
      <polygon points="900,70 1064,38 1064,52 910,86" fill="var(--sky-soft)"/>
      <polygon points="620,404 1064,380 1064,404" fill="var(--sky-soft)"/>
      <path d="M0,0 H846 C836,160 806,300 712,382 C560,400 320,330 160,350 C110,356 70,356 60,360 C52,300 36,284 22,290 C10,296 4,310 0,330 Z" fill="var(--navy-edge)"/>
      <path d="M0,0 H836 C826,160 796,296 700,376 C556,392 320,326 160,346 C110,352 70,352 58,356 C50,298 36,282 22,288 C10,294 4,308 0,326 Z" fill="var(--navy)"/>
    </svg>

    <div class="world-area" role="img" aria-label="Light blue world map"></div>

    <h1 class="title">The Bright Harbour Crew</h1>
    <p class="subtitle">Solving online marketing needs</p>
    <ul class="todo-list">
      <li class="todo-item">
        <svg class="tick" viewBox="0 0 24 24" aria-hidden="true"><path d="M3,13 L9,19 L21,6" fill="none" stroke="var(--white)" stroke-width="4" stroke-linecap="round" stroke-linejoin="round"/></svg>
        Making web sites ‘sticky’
      </li>
      <li class="todo-item">
        <svg class="tick" viewBox="0 0 24 24" aria-hidden="true"><path d="M3,13 L9,19 L21,6" fill="none" stroke="var(--white)" stroke-width="4" stroke-linecap="round" stroke-linejoin="round"/></svg>
        Increasing conversions
      </li>
      <li class="todo-item">
        <svg class="tick" viewBox="0 0 24 24" aria-hidden="true"><path d="M3,13 L9,19 L21,6" fill="none" stroke="var(--white)" stroke-width="4" stroke-linecap="round" stroke-linejoin="round"/></svg>
        Boosting quality traffic
      </li>
    </ul>

    <div class="brand">
      <span class="brand-dot"></span>
      <span class="brand-name">TALLOWFINCH HUB</span>
    </div>
  </section>
</div>
</body>
</html>
```